Marketing Graphics for App

We need a feature graphic to be used in an app store listing for the app Quill Puzzles Plus. Quill Puzzles Plus is a brain training app that allows people to practice various cognitive skills. Our immediate need is for a graphic that can be scaled to run on the Verano Shop Hub free app of the day promotion. This ad will show up on the lock screen on the Tolvo Slate that users will see when the Tolvo Slate is turned on before it is unlocked.

We need a layered PSD file, so that internal elements can be scaled/moved. Please see the guidelines for the graphics ads from Verano.

Concept style guide: https://media-cdn.verano-example.com/docs/ads/VeranoLockCreativeRules.pdf

Technical style guide: https://media-cdn.verano-example.com/docs/ads/VeranoTolvoSlateAdGuide.pdf

I have included some of our existing graphics assets.

See also the app store listing:
http://www.verano-example.com/shop/item/Q77RTWPLMN

Target Market(s)

Mobile phone app users.

Industry/Entity Type

Training

Requirements
Must have
• Text: Quill Puzzles Plus

Text: Exercise Your Brain
Possibly add: Brain Training Games

```html
<!DOCTYPE html>
<html lang="en">
<head>
<meta charset="utf-8">
<title>Quill Puzzles Plus – Lock Screen Feature Graphic</title>
<link rel="stylesheet" href="https://fonts.googleapis.com/css2?family=PT+Sans:wght@700&family=Short+Stack&display=swap">
<style>
  :root {
    --sky-light: #48c9f0;
    --sky-mid: #1a93d6;
    --sky-deep: #0a5aa8;
    --glow: #e9f8ff;
    --brain-light: #bfe3f7;
    --brain-mid: #6fa9dc;
    --brain-deep: #2f6fb4;
    --pill-top: #5a5855;
    --pill-bottom: #2b2a28;
    --pill-edge: rgba(255,255,255,0.85);
    --text-light: #ffffff;
  }
  html, body {
    margin: 0;
    padding: 0;
    width: 1200px;
    height: 843px;
    overflow: hidden;
    background: var(--sky-deep);
  }
  .feature-graphic {
    position: relative;
    width: 1200px;
    height: 843px;
    overflow: hidden;
    background:
      radial-gradient(ellipse 520px 420px at 52% 22%, var(--sky-light) 0%, rgba(72,201,240,0) 70%),
      linear-gradient(160deg, var(--sky-mid) 0%, #1686cc 45%, var(--sky-deep) 100%);
  }
  .orbit-lines {
    position: absolute;
    inset: 0;
    width: 1200px;
    height: 843px;
  }
  .brain-glow {
    position: absolute;
    left: 600px;
    top: 345px;
    width: 620px;
    height: 620px;
    transform: translate(-50%, -50%);
    border-radius: 50%;
    background: radial-gradient(circle, rgba(255,255,255,0.75) 0%, rgba(200,240,255,0.35) 35%, rgba(120,210,245,0) 70%);
  }
  .brain-art {
    position: absolute;
    left: 408px;
    top: 120px;
    width: 384px;
    height: 440px;
    border-radius: 48% 48% 44% 44% / 46% 46% 54% 54%;
    background: radial-gradient(ellipse at 45% 35%, var(--brain-light) 0%, var(--brain-mid) 55%, var(--brain-deep) 100%);
    box-shadow: 0 0 0 8px var(--glow);
  }
  .app-title {
    position: absolute;
    left: 0;
    right: 0;
    top: 600px;
    margin: 0;
    text-align: center;
    font-family: "PT Sans", sans-serif;
    font-weight: 700;
    font-size: 66px;
    letter-spacing: -1px;
    color: var(--text-light);
    line-height: 1;
  }
  .tagline {
    position: absolute;
    left: 0;
    right: 0;
    top: 692px;
    margin: 0;
    text-align: center;
    font-family: "Short Stack", cursive;
    font-size: 40px;
    color: var(--text-light);
    line-height: 1;
  }
  .pill {
    position: absolute;
    top: 591px;
    height: 108px;
    background: linear-gradient(180deg, var(--pill-top) 0%, var(--pill-bottom) 100%);
    display: flex;
    align-items: center;
    justify-content: center;
    box-sizing: border-box;
  }
  .pill-learn {
    left: 0;
    width: 178px;
    border-radius: 0 54px 54px 0;
    border: 2px solid var(--pill-edge);
    border-left: none;
    font-family: "PT Sans", sans-serif;
    font-weight: 700;
    font-size: 17px;
    color: var(--text-light);
    padding-right: 18px;
  }
  .pill-unlock {
    right: 0;
    width: 176px;
    border-radius: 54px 0 0 54px;
    border: 2px solid var(--pill-edge);
    border-right: none;
    padding-right: 20px;
  }
</style>
</head>
<body>
  <main class="feature-graphic">
    <svg class="orbit-lines" viewBox="0 0 1200 843" aria-hidden="true">
      <ellipse cx="600" cy="360" rx="560" ry="470" fill="none" stroke="rgba(255,255,255,0.08)" stroke-width="3"/>
      <ellipse cx="600" cy="360" rx="480" ry="400" fill="none" stroke="rgba(255,255,255,0.06)" stroke-width="2"/>
    </svg>

    <div class="brain-glow"></div>
    <div class="brain-art" role="img" aria-label="Illustration of a blue human brain viewed from the front, glowing"></div>

    <div class="pill pill-learn">Learn More</div>
    <div class="pill pill-unlock" aria-label="Unlock">
      <svg width="30" height="36" viewBox="0 0 30 36" aria-hidden="true">
        <path d="M8 15 V10 a7 7 0 0 1 14 0 V15" fill="none" stroke="#ffffff" stroke-width="4"/>
        <rect x="3" y="15" width="24" height="19" rx="2" fill="#ffffff"/>
        <circle cx="15" cy="23" r="3" fill="#3a3937"/>
        <rect x="13.5" y="23" width="3" height="6" fill="#3a3937"/>
      </svg>
    </div>

    <h1 class="app-title">QUILL PUZZLES PLUS</h1>
    <p class="tagline">" exercise your brain "</p>
  </main>
</body>
</html>
```